Poster design for a vet clinic

Running a campaign called 'Tail teller', which is where people get a $30 voucher for themselves and their friend if they refer somebody to our vet clinic.

Text something like:
We love Tail Tellers!
Refer a fur friend to our friendly team and both your fur child and their fur child will receive a $30 voucher to use in clinic! *
* Limited to one pet per fur parent and the referred fur parent must be new to our clinic. Unlimited vouchers for number of referrals!

I want it to be cute but professional. You can see the design styles at mossbury-vet.com.au/kelvale and see the logo there too.
I am thinking of having a dog whispering to a cat or something like that as the main image.
I would like both the photoshop file and the pdf please. Would be for an A2 poster.

```html
<!DOCTYPE html>
<html lang="en">
<head>
<meta charset="utf-8">
<title>Mossbury Vet – Tail Tellers referral poster</title>
<link rel="stylesheet" href="https://fonts.googleapis.com/css2?family=Oswald:wght@500;700&family=Montserrat:wght@500;600&display=swap">
<style>
  :root {
    --stage: #3a3a3c;
    --paper: #ffffff;
    --paper-tint: #f3f3f3;
    --cocoa: #6b4f45;
    --orange: #f28a0f;
    --heart: #ff0000;
    --ticket: #f2bb58;
    --ink: #222222;
    --follow-bar: #ececec;
    --photo-light: #efe6dc;
    --photo-mid: #b8926a;
  }
  * { box-sizing: border-box; margin: 0; padding: 0; }
  html, body { width: 1200px; height: 1200px; overflow: hidden; }
  body { background: var(--stage); position: relative; font-family: "Montserrat", sans-serif; }

  .poster {
    position: absolute; left: 203px; top: 40px;
    width: 794px; height: 1120px;
    background: var(--paper-tint);
    overflow: hidden;
  }

  .brand { position: absolute; left: 0; right: 0; top: 44px; text-align: center; }
  .brand-name {
    font-family: "Oswald", sans-serif; font-weight: 700;
    font-size: 46px; line-height: 1; color: var(--orange); letter-spacing: 1px;
  }
  .brand-rule { width: 180px; height: 2px; background: var(--orange); margin: 10px auto 6px; }
  .brand-location {
    font-family: "Montserrat", sans-serif; font-weight: 500;
    font-size: 18px; color: var(--orange); letter-spacing: 0.5px;
  }

  .hero-photo {
    position: absolute; left: 40px; top: 185px; width: 706px; height: 470px;
    border-radius: 46% 46% 10px 10px / 40% 40% 10px 10px;
    background: radial-gradient(ellipse at 60% 55%, var(--photo-mid) 0%, var(--photo-light) 70%);
  }

  .headline-band {
    position: absolute; left: 0; top: 633px; width: 100%; height: 197px;
    background: var(--cocoa);
  }
  .headline-we {
    position: absolute; left: 80px; top: 18px;
    font-family: "Oswald", sans-serif; font-weight: 700;
    font-size: 150px; line-height: 1; color: var(--paper); letter-spacing: -2px;
  }
  .headline-heart { position: absolute; left: 290px; top: 46px; width: 134px; height: 124px; }
  .headline-name {
    position: absolute; left: 441px; top: 38px;
    font-family: "Oswald", sans-serif; font-weight: 700;
    font-size: 62px; line-height: 1.14; color: var(--paper);
  }

  .offer { position: absolute; left: 0; top: 830px; width: 100%; height: 175px; background: var(--paper); }
  .voucher { position: absolute; left: 40px; top: 15px; width: 336px; height: 144px; }
  .voucher-label {
    position: absolute; left: 68px; top: 34px; width: 288px; height: 106px;
    display: flex; align-items: center; justify-content: center;
    font-family: "Oswald", sans-serif; font-weight: 500;
    font-size: 46px; line-height: 1; color: var(--ink); letter-spacing: -1px;
    white-space: nowrap;
  }
  .offer-copy { position: absolute; left: 399px; top: 24px; width: 370px; }
  .offer-title {
    font-family: "Oswald", sans-serif; font-weight: 700;
    font-size: 44px; line-height: 1; color: var(--orange); white-space: nowrap;
  }
  .offer-text {
    margin-top: 12px; font-size: 17.5px; line-height: 24px;
    color: var(--ink); font-weight: 500; letter-spacing: 0.2px; white-space: nowrap;
  }

  .follow {
    position: absolute; left: 0; top: 1005px; width: 100%; height: 45px;
    background: var(--follow-bar);
    display: flex; align-items: center; justify-content: center; gap: 14px;
    font-size: 21px; font-weight: 600; color: var(--ink); letter-spacing: 1px;
  }
  .social { display: flex; align-items: center; gap: 6px; font-size: 16px; font-weight: 600; color: var(--orange); letter-spacing: 0; }
  .social-dot { width: 12px; height: 12px; border-radius: 50%; background: var(--orange); }

  .terms {
    position: absolute; left: 0; top: 1050px; width: 100%; height: 70px;
    background: var(--cocoa); color: var(--paper);
    display: flex; flex-direction: column; align-items: center; justify-content: center;
    font-size: 15.5px; line-height: 20px; font-weight: 500; text-align: center;
  }
</style>
</head>
<body>
  <main class="poster">
    <header class="brand">
      <div class="brand-name">Mossbury Vet</div>
      <div class="brand-rule"></div>
      <div class="brand-location">KELVALE</div>
    </header>

    <div class="hero-photo" role="img" aria-label="Photo of a tabby kitten and a shepherd puppy sitting side by side, the puppy whispering to the cat"></div>

    <section class="headline-band">
      <div class="headline-we">WE</div>
      <svg class="headline-heart" viewBox="0 0 134 124" aria-label="love">
        <path d="M67 122 C40 95 2 72 2 38 C2 16 18 2 37 2 C51 2 61 10 67 22 C73 10 83 2 97 2 C116 2 132 16 132 38 C132 72 94 95 67 122 Z" fill="var(--heart)"/>
      </svg>
      <div class="headline-name">TAIL<br>TELLERS!</div>
    </section>

    <section class="offer">
      <svg class="voucher" viewBox="0 0 336 144" aria-hidden="true">
        <path d="M12 0 H324 V10 L330 16 L324 22 L330 28 L324 34 L330 40 L324 46 L330 52 L324 58 L330 64 L324 70 L330 76 L324 82 L330 88 L324 94 L330 100 L324 106 L330 112 L324 118 L330 124 L324 130 V144 H12 V130 L6 124 L12 118 L6 112 L12 106 L6 100 L12 94 L6 88 L12 82 L6 76 L12 70 L6 64 L12 58 L6 52 L12 46 L6 40 L12 34 L6 28 L12 22 L6 16 L12 10 Z" fill="var(--ticket)"/>
        <rect x="28" y="19" width="288" height="106" rx="12" fill="none" stroke="var(--ink)" stroke-width="3"/>
      </svg>
      <div class="voucher-label">$30 VOUCHER</div>
      <div class="offer-copy">
        <div class="offer-title">REFER A FUR FRIEND</div>
        <p class="offer-text">to our friendly team and both your<br>fur child &amp; their fur child will receive<br>a $30 voucher to use in clinic.*</p>
      </div>
    </section>

    <div class="follow">
      <span>FOLLOW US:</span>
      <span class="social"><span class="social-dot"></span>Snapfeed</span>
      <span class="social"><span class="social-dot"></span>Friendbook</span>
    </div>

    <footer class="terms">
      <span>* Limited to one pet per fur parent &amp; the referred fur parent must be new to our clinic.</span>
      <span>Unlimited vouchers for number of referrals!</span>
    </footer>
  </main>
</body>
</html>
```